Verlotti Magician

I want the business card for my business to give to people who watch that later I will be employed to show magic here is my website http://www.verlottimagicien.net/I want the interesting design , i am very opened for formal and informal, I watch a lot of design so don't stick to the common shape and form but i hope it can also be produced the thing to write on will be the same as in picture that i will upload , i also will upload the logo for you that so can be easy to useDenis CostilleMagicianMAGICIAN BALSAMO 17 rue des Tilleuls - 48210 VAUBRESSE contact@verlottimagicien.net tel. 0384 519 467 tel. 0672 904 153

```html
<!DOCTYPE html>
<html lang="fr">
<head>
<meta charset="utf-8">
<title>Verlotti Magician – Business Card</title>
<link rel="stylesheet" href="https://fonts.googleapis.com/css2?family=Jost:wght@400;500;600&family=PT+Sans:wght@400&display=swap">
<style>
  :root {
    --backdrop: #2a2a2b;
    --card: #ffffff;
    --accent: #d2302a;
    --ink: #1c1c1c;
    --rule: #9a9a9a;
    --figure-dark: #141414;
    --figure-mid: #3a3a3a;
  }
  * { margin: 0; padding: 0; box-sizing: border-box; }
  html, body {
    width: 1200px;
    height: 900px;
    overflow: hidden;
    background: var(--backdrop);
  }
  .canvas {
    position: relative;
    width: 1200px;
    height: 900px;
  }
  .card {
    position: absolute;
    left: 320px;
    width: 560px;
    height: 320px;
    background: var(--card);
    border-bottom: 9px solid var(--accent);
    overflow: hidden;
  }
  .card--front { top: 110px; }
  .card--back { top: 470px; }

  /* Front */
  .brand {
    position: absolute;
    left: 0;
    right: 0;
    top: 52px;
    display: flex;
    flex-direction: column;
    align-items: center;
  }
  .brand__figure {
    width: 150px;
    height: 132px;
    border-radius: 40px 40px 6px 6px;
    background: linear-gradient(180deg, var(--figure-mid) 0%, var(--figure-dark) 100%);
  }
  .brand__name {
    margin-top: 16px;
    font-family: "Jost", sans-serif;
    font-weight: 400;
    font-size: 26px;
    letter-spacing: 3px;
    color: var(--ink);
    text-transform: uppercase;
  }

  /* Back */
  .holder {
    position: absolute;
    top: 118px;
    right: 275px;
    text-align: right;
    white-space: nowrap;
  }
  .holder__name {
    font-family: "Jost", sans-serif;
    font-weight: 600;
    font-size: 21px;
    color: var(--accent);
    text-transform: uppercase;
    line-height: 1.1;
  }
  .holder__role {
    font-family: "PT Sans", sans-serif;
    font-size: 14px;
    color: var(--ink);
    margin-top: 2px;
  }
  .divider {
    position: absolute;
    left: 298px;
    top: 118px;
    width: 1px;
    height: 74px;
    background: var(--rule);
  }
  .contacts {
    position: absolute;
    left: 312px;
    top: 118px;
    list-style: none;
    font-family: "PT Sans", sans-serif;
    font-size: 15px;
    color: var(--ink);
    line-height: 19px;
    white-space: nowrap;
  }
  .contacts li {
    display: flex;
    align-items: center;
    gap: 6px;
  }
  .contacts svg {
    width: 13px;
    height: 13px;
    flex: none;
    fill: var(--accent);
  }
  .company {
    position: absolute;
    left: 90px;
    width: 330px;
    top: 228px;
    font-family: "PT Sans", sans-serif;
    text-align: center;
  }
  .company__name {
    font-family: "Jost", sans-serif;
    font-weight: 500;
    font-size: 15px;
    color: var(--accent);
    text-transform: uppercase;
  }
  .company__address {
    font-size: 15px;
    color: var(--ink);
  }
</style>
</head>
<body>
<main class="canvas">
  <section class="card card--front" aria-label="Card front">
    <div class="brand">
      <div class="brand__figure" role="img" aria-label="Illustration of the magician in a dark jacket holding playing cards"></div>
      <p class="brand__name">Verlotti Magician</p>
    </div>
  </section>

  <section class="card card--back" aria-label="Card back">
    <div class="holder">
      <p class="holder__name">Hugo Marsenac</p>
      <p class="holder__role">Magician</p>
    </div>
    <div class="divider"></div>
    <ul class="contacts">
      <li>
        <svg viewBox="0 0 16 16" aria-hidden="true"><path d="M2 5c0-2 2-3 6-3s6 1 6 3v1.5h-3.5V5h-5v1.5H2z"/><rect x="3" y="8" width="10" height="6" rx="1"/></svg>
        0384 519 467
      </li>
      <li>
        <svg viewBox="0 0 16 16" aria-hidden="true"><path d="M2 5c0-2 2-3 6-3s6 1 6 3v1.5h-3.5V5h-5v1.5H2z"/><rect x="3" y="8" width="10" height="6" rx="1"/></svg>
        0672 904 153
      </li>
      <li>
        <svg viewBox="0 0 16 16" aria-hidden="true"><rect x="1" y="3" width="14" height="10" rx="1"/><path d="M1.5 4 8 9l6.5-5" stroke="#fff" stroke-width="1.4" fill="none"/></svg>
        contact@verlottimagicien.net
      </li>
      <li>
        <svg viewBox="0 0 16 16" aria-hidden="true"><circle cx="8" cy="8" r="7"/><path d="M1 8h14M8 1c-3 3.5-3 10.5 0 14M8 1c3 3.5 3 10.5 0 14" stroke="#fff" stroke-width="1" fill="none"/></svg>
        www.verlottimagicien.net
      </li>
    </ul>
    <div class="company">
      <p class="company__name">Magician Verlotti</p>
      <p class="company__address">17 rue des Tilleuls - 48210 VAUBRESSE</p>
    </div>
  </section>
</main>
</body>
</html>
```